We are looking for some title pages for a children journal, we like the designs attached with use of photos and design elements particularly angles and shapes, we like drawings, icons and photos incroprated but not cartoon like.
Some photos attached to work with

Page 1)
Maple & Finch logo
incorporate the image with the MFB letters and rainbow

wording
My Learning Journal
2026
have a blank box to write the child's
have a name box

Page 2
wording
Finch pathway curriculum
Include the logos in the Finch Pathwya curriculum

```html
<!DOCTYPE html>
<html lang="en">
<head>
<meta charset="utf-8">
<title>Maple &amp; Finch – My Learning Journal 2026</title>
<link href="https://fonts.googleapis.com/css2?family=Gochi+Hand&family=Montserrat:wght@700;800&family=Roboto:wght@400&display=swap" rel="stylesheet">
<style>
  :root{
    --stage:#232323;
    --sky:#0aa5e2;
    --sun:#ffec00;
    --white:#ffffff;
    --ink:#2a2a2a;
    --grass:#8cc63f;
    --grass-light:#a6d65a;
    --rule:#7fd0f0;
  }
  *{box-sizing:border-box;margin:0;padding:0}
  html,body{width:769px;height:1200px;overflow:hidden;background:var(--stage)}
  .spread{position:absolute;top:341px;left:11px;display:flex;gap:14px}
  .page{position:relative;width:366px;height:518px;overflow:hidden}

  /* Cover */
  .cover{background:var(--sky)}
  .page-shapes{position:absolute;inset:0}
  .brand{position:absolute;top:38px;left:0;width:100%;display:flex;justify-content:center;align-items:center;gap:7px}
  .brand-dot{width:14px;height:14px;border-radius:50%;background:var(--sun)}
  .brand-name{font-family:"Montserrat",sans-serif;font-weight:800;font-size:19px;color:var(--white);letter-spacing:.3px}
  .school-mark{position:absolute;left:48px;top:272px;display:flex;align-items:center;gap:6px}
  .school-dot{width:12px;height:12px;border-radius:50%;background:var(--white)}
  .school-name{font-family:"Montserrat",sans-serif;font-weight:800;font-size:22px;color:var(--white)}
  .title{position:absolute;top:352px;width:100%;text-align:center;color:var(--white);font-weight:400}
  .title-script{display:block;font-family:"Gochi Hand",cursive;font-size:42px;line-height:1}
  .title-year{display:block;font-family:"Montserrat",sans-serif;font-weight:800;font-size:26px;line-height:1.05;margin-top:-2px}
  .name-box{position:absolute;left:32px;top:440px;width:302px;height:54px;background:var(--white);border-radius:9px;padding:13px 17px 0}
  .name-line{height:1px;background:var(--rule);margin-bottom:19px}

  /* Curriculum page */
  .curriculum{background:var(--white)}
  .curriculum-title{position:absolute;top:8px;width:100%;text-align:center;font-family:"Gochi Hand",cursive;font-weight:400;font-size:24px;color:var(--white)}
  .pillar{position:absolute;left:17px;width:336px;display:flex;gap:11px}
  .pillar-icon{flex:none;width:52px;height:52px;border-radius:50%;border:3px solid var(--sky);padding:3px;margin-top:4px}
  .pillar-icon span{display:block;width:100%;height:100%;border-radius:50%}
  .pillar-body{width:262px}
  .pillar-name{font-family:"Gochi Hand",cursive;font-weight:400;font-size:13px;color:var(--sky);line-height:1.1}
  .pillar-text{font-family:"Roboto",sans-serif;font-size:5.3px;line-height:1.3;color:var(--ink);text-align:justify}
  .site{position:absolute;bottom:5px;width:100%;text-align:center;font-family:"Gochi Hand",cursive;font-size:16px;color:var(--white)}
</style>
</head>
<body>
<div class="spread">

  <section class="page cover">
    <svg class="page-shapes" width="366" height="518" viewBox="0 0 366 518">
      <defs>
        <linearGradient id="room" x1="0" y1="0" x2="1" y2="1">
          <stop offset="0" stop-color="#e9e4dc"/>
          <stop offset=".5" stop-color="#c9a47a"/>
          <stop offset="1" stop-color="#8a6446"/>
        </linearGradient>
      </defs>
      <path d="M0 66 Q160 96 366 40 L366 80 Q180 118 0 102 Z" fill="var(--sun)"/>
      <g role="img" aria-label="Photo of a classroom with a wooden peg board showing a bead rainbow and the MFB letters">
        <path d="M0 94 Q180 112 366 64 L366 330 Q180 360 0 398 Z" fill="url(#room)"/>
      </g>
      <path d="M0 384 Q180 330 366 316 L366 336 Q180 346 0 414 Z" fill="var(--sun)"/>
      <path d="M0 404 Q180 340 366 332 L366 518 L0 518 Z" fill="var(--sky)"/>
    </svg>
    <div class="brand"><span class="brand-dot"></span><span class="brand-name">Maple &amp; Finch</span></div>
    <div class="school-mark"><span class="school-dot"></span><span class="school-name">MFB</span></div>
    <h1 class="title"><span class="title-script">My Learning</span><span class="title-year">JOURNAL 2026</span></h1>
    <div class="name-box"><div class="name-line"></div><div class="name-line"></div></div>
  </section>

  <section class="page curriculum">
    <svg class="page-shapes" width="366" height="518" viewBox="0 0 366 518">
      <path d="M0 0 H366 V30 Q180 34 0 32 Z" fill="var(--sky)"/>
      <path d="M0 32 Q180 34 366 30 L366 34 Q190 44 0 56 Z" fill="var(--sun)"/>
      <path d="M0 32 Q180 34 366 30 L366 32 Q190 40 0 44 Z" fill="var(--sky)"/>
      <path d="M0 492 Q180 466 366 490 L366 518 L0 518 Z" fill="var(--grass)"/>
      <path d="M0 494 Q180 470 366 492 L366 496 Q180 476 0 500 Z" fill="var(--grass-light)"/>
    </svg>
    <h2 class="curriculum-title">Finch pathway curriculum</h2>

    <article class="pillar" style="top:66px">
      <div class="pillar-icon"><span role="img" aria-label="Icon of a stack of books" style="background:linear-gradient(135deg,#f6b93b,#e55039)"></span></div>
      <div class="pillar-body">
        <h3 class="pillar-name">Smart Start</h3>
        <p class="pillar-text">Knowing that 90% of the human brain is developed in the first five years of life really reinforces what an important job we have in challenging and stimulating your child each day. Our Smart Start program is all about the cognitive development of your child. We deliver pre-reading, pre-writing, maths, science, problem-solving and geography education, all appropriate to your child's specific age and developmental stage. Unique to MFB, our centres each contain a Smart Start room. This is a thoughtfully-designed, separate learning space where children go in small groups to participate in learning experiences on the Lumora LED Panel, participate in Word Sprouts and a variety of school readiness and focused learning experiences.</p>
      </div>
    </article>

    <article class="pillar" style="top:143px">
      <div class="pillar-icon"><span role="img" aria-label="Icon of a paint palette and music note" style="background:linear-gradient(135deg,#fbc531,#0aa5e2)"></span></div>
      <div class="pillar-body">
        <h3 class="pillar-name">Inspired</h3>
        <p class="pillar-text">The Inspired element of our curriculum is all about promoting creativity, exploration and inspiration in children. Creative play and artistic activities have a central role in children's learning and development. Drama, music, dance and visual arts foster creativity, nurture the imagination and develop problem-solving, thinking and motor skills. We have also developed outdoor classrooms in our services as there are many proven benefits to spending time outdoors. Children have an innate connection with nature and we want them to enjoy and respect the beauty of the outdoors. This is why environmental awareness and sustainability are also a core part of our Inspired program, because we want children to connect with nature and become environmental advocates. You will see this in practice through our educational programs, green thumb gardening lessons and sustainable practices.</p>
      </div>
    </article>

    <article class="pillar" style="top:232px">
      <div class="pillar-icon"><span role="img" aria-label="Icon of two hands forming a heart" style="background:linear-gradient(135deg,#ffdd00,#f08a24)"></span></div>
      <div class="pillar-body">
        <h3 class="pillar-name">Unite</h3>
        <p class="pillar-text">Our Unite program is about teaching children to be socially responsible towards others and the environment, learn compassion, kindness and respect for diversity. This involves weaving diversity into the fabric of children's everyday lives, talking openly about identity and heritage and affirming the rich diversity of our community backgrounds. This helps children make bridges across cultures and traditions and builds positive identities and a respect for differences. We enjoy engaging and connecting with our community through family social gatherings, community visitors, incursions and participation in community and cultural events. We regularly host events, information evenings and seminars for our families to keep connected and offer them support.</p>
      </div>
    </article>

    <article class="pillar" style="top:314px">
      <div class="pillar-icon"><span role="img" aria-label="Icon of a heart with a pulse line and fruit" style="background:linear-gradient(135deg,#e84118,#fbc531)"></span></div>
      <div class="pillar-body">
        <h3 class="pillar-name">Fit</h3>
        <p class="pillar-text">With the obesity epidemic becoming a worldwide health issue, we believe it's important to teach children how to nurture their bodies from a young age. Our Fit program educates children about their physical wellbeing and encourages them to take responsibility for their own health. You will see this in practice through our daily educational programs, physical health checks, little bakers cooking lessons, Crunch &amp; Hop program, gardening classes and nutritious home-cooked meals. Each day children also participate in sports, yoga or dance classes which are run by our qualified instructors.</p>
      </div>
    </article>

    <article class="pillar" style="top:383px">
      <div class="pillar-icon"><span role="img" aria-label="Icon of a circle of people" style="background:linear-gradient(135deg,#44bd32,#e84118)"></span></div>
      <div class="pillar-body">
        <h3 class="pillar-name">Crew</h3>
        <p class="pillar-text">When we think back to our pre-school or primary school years, we usually recall a fantastic teacher who encouraged and nurtured us as children. When we recruit educators at Maple and Finch Kindergarten, we don't only look at their experience and qualifications, we look for passionate and nurturing people who will create wonderful memories for each and every child. We offer professional development to support their growth and development, progression opportunities to support their careers and a supportive team environment because we know if they are happy, the children are happy. We also know when they are confident in their skills, their passion an enthusiasm is contagious and creates a fun and nurturing environment for the children. That's why our crew are a really important element of our Finch Pathway program.</p>
      </div>
    </article>

    <p class="site">www.mapleandfinch.edu.au</p>
  </section>

</div>
</body>
</html>
```